Thistlewood Group Business Card Design

We are looking for a new business card design, we are not happy with our current design. We are a boutique management consulting firm and our clients are typically meridian 400 companies.

I have attached the current front and back that we have as well as a version of our logo that can be used. I am trying to get a higher resolution version of the logo file to upload to the project.

Target Market(s)

Meridian 400 companies are our primary client base. Financial services, life sciences, pharmaceuticals and telecom companies are

Industry/Entity Type

Management Consulting

Contact Information for Business Card

We are trying to communicate a high degree of professionalism, a somewhat minimalist perhaps with some air of whimsy (without overdoing it). Attached is the current design, front and back as well as logos. I like the current back of the card and assume we will keep the phrase the same.

From a color palette perspective, I prefer to stay with a gray scale as they are today.

Font styles to use
Sans Serif

Colors
1b1b1b
474747
ffffff

Requirements
Must have
• Two sided business card design. File format should be something that can be used outside of Photoshop like MS Publisher so that they can be edited with personal information.
• Font should be calibri or something very similar and should be available within MS Office
Should not have
• No other logos or graphics outside of the logo provided.

```html
<!DOCTYPE html>
<html lang="en">
<head>
<meta charset="utf-8">
<title>Thistlewood Group Business Card</title>
<link rel="stylesheet" href="https://fonts.googleapis.com/css2?family=Open+Sans:wght@400;600;700&display=swap">
<style>
  :root {
    --ink: #1b1b1b;
    --ink-soft: #474747;
    --paper: #ffffff;
    --card-dark: #262626;
    --stage: #e6e6e6;
  }
  * { box-sizing: border-box; margin: 0; padding: 0; }
  html, body { width: 1200px; height: 1000px; overflow: hidden; }
  body {
    background: var(--stage);
    font-family: "Open Sans", sans-serif;
    position: relative;
  }
  .card {
    position: absolute;
    left: 265px;
    width: 665px;
    height: 397px;
    border-radius: 24px;
    overflow: hidden;
  }
  .card-front { top: 73px; background: var(--paper); color: var(--ink); }
  .card-back { top: 532px; background: var(--card-dark); color: var(--paper); }

  .brand {
    position: absolute;
    left: 33px;
    top: 38px;
    display: flex;
    align-items: center;
    gap: 12px;
  }
  .brand-dot {
    width: 34px; height: 34px;
    border-radius: 50%;
    background: var(--ink);
  }
  .brand-name {
    font-size: 48px;
    font-weight: 600;
    letter-spacing: -0.5px;
    line-height: 1;
    color: var(--ink);
  }
  .tm { font-size: 10px; font-weight: 600; vertical-align: top; margin-left: 2px; }

  .contact {
    position: absolute;
    left: 374px;
    top: 138px;
    font-size: 15.5px;
    line-height: 20px;
    color: var(--ink);
  }
  .person-name { font-size: 21px; font-weight: 700; letter-spacing: 0.3px; line-height: 24px; }
  .person-title { margin-bottom: 22px; }
  .company { font-weight: 700; }
  .address { margin-bottom: 10px; }
  .contact-line { display: flex; align-items: center; gap: 6px; line-height: 23px; }
  .contact-line svg { width: 15px; height: 15px; fill: var(--ink); flex: none; }
  .web-domain { font-weight: 700; }

  .back-brand {
    position: absolute;
    right: 42px;
    top: 278px;
    text-align: right;
  }
  .back-name {
    font-size: 62px;
    font-weight: 600;
    letter-spacing: -0.5px;
    line-height: 1;
    color: var(--paper);
  }
  .back-name .tm { font-size: 11px; }
  .tagline {
    margin-top: 14px;
    font-size: 13.5px;
    color: var(--paper);
  }
</style>
</head>
<body>
  <section class="card card-front" aria-label="Business card front">
    <div class="brand">
      <span class="brand-dot"></span>
      <span class="brand-name">Thistlewood<span class="tm">TM</span></span>
    </div>

    <div class="contact">
      <div class="person-name">OWEN HALE</div>
      <div class="person-title">Managing Director</div>
      <div class="company">Thistlewood Group, Inc.</div>
      <div class="address">218 Larkmoor Avenue<br>Suite 207<br>Ashcombe Is., WA 98345</div>
      <div class="contact-line">
        <svg viewBox="0 0 16 16" aria-hidden="true"><path d="M1 5c0-2 3-3 7-3s7 1 7 3v1h-3V5H4v1H1zM4 7h8l2 6H2z"/></svg>
        <span>206.555.0148</span>
      </div>
      <div class="contact-line">
        <svg viewBox="0 0 16 16" aria-hidden="true"><path d="M1 3h14v10H1zM2.5 4.5 8 9l5.5-4.5v-.2H2.5z" fill-rule="evenodd"/></svg>
        <span>ohale@thistlewoodgroup.com</span>
      </div>
      <div class="contact-line">
        <svg viewBox="0 0 16 16" aria-hidden="true"><path d="M8 1a7 7 0 1 0 0 14A7 7 0 0 0 8 1zm0 2a5 5 0 0 1 0 10A5 5 0 0 1 8 3z" fill-rule="evenodd"/><path d="M7 7h2v6H7zM5 7h6v1.5H5z"/></svg>
        <span>www.<span class="web-domain">thistlewoodgroup</span>.com</span>
      </div>
    </div>
  </section>

  <section class="card card-back" aria-label="Business card back">
    <div class="back-brand">
      <div class="back-name">Thistlewood<span class="tm">TM</span></div>
      <div class="tagline">The prefered choice for leaders top priorities</div>
    </div>
  </section>
</body>
</html>
```